Purchasing Management Consulting B to B Web Design PAYMENT GUARANTY

We'd like to build a new digital image for our website.

Our company is managing purchasing consultancy services for Large and Medium companies around 4 activities :
- Procurement outsourcing
- Purchasing consulting (cost reduction)
- Supply chain training
- Web platform to manage Supplier risk (TrusoMark.com)

We now aim to harmonies our website in term of design in order to build a strongest Corporate Image.

SEE REQUIREMENT ENCLOSED

Please have a look on our current websites:
- www.procuvantix.com
- www.pqz-network.com
- www.trusomark.com

Reason: Hello, Some project received are not really professional and need more details. I did not see all deliverable requested in specifications. I'll revert to designer to improve design. Regards, Bastien

Reason: Only few designers reply and feedback still need to be done.

Target Market(s)

Our business is exclusively Business to Business toward Medium and Large companies.

Industry/Entity Type

Digital

Requirements
Must have
• Website will be developped in Joomla CMS.
The user community will use Fellowkit module : Visitor should be "influenced" to communicate its contact details by registering the community.

Ergonomy, Simplicity and professionnalism is the key objectives.

Deliverables :
- Corporate Home page including clear access to our 4 activities
- Dynamique banner
- Corporate article / contact pages (1 or 2)
- Activities home pages (x 4)
- Activity Catalog (Indesign for paper version)
Nice to have
• Integration of Design for our consulting and training catalog will be interesting.

Livechat design (the one of Craftplaza.com is good)
Should not have
• Only psd

Not html

```html
<!DOCTYPE html>
<html lang="fr">
<head>
<meta charset="utf-8">
<title>Procuvantix – Achetez en toute simplicité</title>
<link href="https://fonts.googleapis.com/css2?family=Open+Sans:ital,wght@0,400;0,600;0,700;1,400;1,700&family=Raleway:wght@300;400;600&display=swap" rel="stylesheet">
<style>
:root{
  --nav:#5b5868;
  --orange:#d9901a;
  --gold:#f2b525;
  --gold-dark:#e09a12;
  --lime:#c3c81a;
  --lime-dark:#a8ad0c;
  --ink:#3c3c3c;
  --text:#333;
  --panel-line:#dcdcdc;
}
*{box-sizing:border-box;margin:0;padding:0}
html,body{width:1200px;height:1148px;overflow:hidden}
body{position:relative;background:#fff;font-family:Arial,"Open Sans",sans-serif;color:var(--text)}
.abs{position:absolute}

.masthead{position:absolute;left:0;top:0;width:1200px;height:612px;
  background:linear-gradient(#fff 0,#f5f5f5 160px,#e4e4e4 480px,#d6d6d6 612px)}

.brand{position:absolute;left:104px;top:30px;display:flex;align-items:center;gap:10px}
.brand-disc{width:36px;height:36px;border-radius:50%;background:var(--lime)}
.brand-name{font-family:"Open Sans",sans-serif;font-weight:700;font-size:34px;color:var(--nav);letter-spacing:1px}

.lang{left:936px;top:21px;width:161px;height:32px;border:1px solid #ddd;border-radius:3px;background:#fbfbfb;
  font:400 14px "Open Sans",sans-serif;color:#333;display:flex;align-items:center;padding-left:12px;gap:10px}
.flag{display:flex;width:22px;height:15px}
.flag i{flex:1}
.caret{position:absolute;right:8px;top:7px;width:17px;height:17px;background:#6b6877;border:1px solid #444}

.nav{left:290px;top:66px;width:808px;height:49px;background:var(--nav);border-radius:0 6px 6px 0;
  display:flex;align-items:center;border:1px solid #3e3c48}
.nav a{font:700 17px "Open Sans",sans-serif;color:#fff;text-decoration:none;padding:0 31px;border-right:1px solid #7a7786;line-height:22px}
.nav a:first-child{padding-left:29px}
.nav a:last-child{border:none}

.field{top:131px;width:141px;height:31px;border:1px solid #d8d8d8;background:#fff;font:13px Arial,sans-serif;color:#999;padding:7px 12px}
.login{left:1004px;top:131px;width:86px;height:31px;border:1px solid #c98a0e;border-radius:2px;
  background:linear-gradient(#f8c540,#e9a516);font:700 17px "Open Sans",sans-serif;color:#333;text-align:center;line-height:29px}

.slider{left:101px;top:180px;width:998px;height:363px;background:#fff;box-shadow:0 14px 12px -10px rgba(0,0,0,.35)}
.slide-photo{position:absolute;left:7px;top:6px;width:984px;height:350px;
  background:linear-gradient(90deg,#cfc5b8 0,#e7e1d8 30%,#efeae3 55%,#cdbfae 80%,#8d7c68 100%)}
.slide-caption{position:absolute;left:7px;top:175px;width:550px;height:52px;
  background:linear-gradient(90deg,rgba(70,68,82,.8) 85%,rgba(70,68,82,0));
  font:400 36px "Open Sans",sans-serif;color:#fff;padding-left:20px;line-height:50px}
.dots{left:553px;top:566px;display:flex;gap:8px}
.dots i{width:18px;height:18px;border-radius:50%;border:2px solid #bbb;background:#f3f3f3}
.dots i.on{background:#555;border-color:#ccc}

.promo{left:101px;top:633px;width:998px;height:170px;border-radius:4px;overflow:hidden;border:2px solid #dedede;
  background:linear-gradient(90deg,#b8bd0b,#d5da1c 45%,#b5ba0a 75%)}
.promo-visual{position:absolute;right:0;top:0;width:280px;height:166px;background:linear-gradient(135deg,#f4f4f4,#dcdcdc)}
.promo-line1{position:absolute;left:50px;top:14px;font:300 34px Raleway,sans-serif;color:#fff}
.promo-line2{position:absolute;left:49px;top:50px;font:600 54px Raleway,sans-serif;color:var(--ink)}
.promo-line3{position:absolute;left:237px;top:112px;font:300 36px Raleway,sans-serif;color:#fff}
.promo-btn{position:absolute;left:510px;top:116px;width:180px;height:38px;background:var(--gold);border:2px solid #f7d266;
  font:700 21px "Open Sans",sans-serif;color:#333;text-align:center;line-height:34px}

.card{top:837px;width:231px;height:206px;border:1px solid var(--panel-line);border-radius:4px;background:linear-gradient(#fff,#efefef)}
.card h2{font:400 26px Raleway,sans-serif;color:var(--orange);margin:10px 0 0 21px}
.news-list{list-style:none;margin:9px 0 0 20px}
.news-list li{font:italic 700 13px Arial,sans-serif;color:#333;line-height:24px}
.news-list li::before{content:"";display:inline-block;width:5px;height:5px;border-radius:50%;background:var(--lime-dark);margin-right:7px;vertical-align:middle}
.card p{font:12px/18px Arial,sans-serif;color:#222;margin:11px 14px 0 19px}
.read-more{position:absolute;right:18px;bottom:11px;width:87px;height:20px;background:var(--lime-dark);border-radius:2px;
  font:italic 700 12px Arial,sans-serif;color:#fff;text-align:center;line-height:20px}
.partner-frame{position:absolute;left:35px;top:55px;width:165px;height:104px;border:3px solid #e0e0e0;background:#fff;
  display:flex;align-items:center;justify-content:center;gap:8px}
.partner-frame .brand-disc{width:26px;height:26px}
.partner-frame .brand-name{font-size:26px}
.newsletter p{font:italic 12px/18px Arial,sans-serif;margin:8px 8px 0 15px}
.mail{position:absolute;left:14px;top:93px;width:198px;height:32px;border:1px solid #ccc;background:#fff;border-radius:2px;
  font:italic 12px Arial,sans-serif;color:#aaa;padding:8px 10px}
.mail b{position:absolute;right:3px;top:3px;width:67px;height:24px;background:var(--lime-dark);border-radius:3px;
  font:italic 700 12px Arial,sans-serif;color:#fff;text-align:center;line-height:24px}
.social{position:absolute;left:16px;top:143px;display:flex;gap:10px}
.social i{width:42px;height:42px;border-radius:50%;background:radial-gradient(circle at 40% 35%,#f2f2f2,#9a9a9a);box-shadow:0 2px 3px rgba(0,0,0,.3)}

.footer{left:0;top:1088px;width:1200px;height:60px;background:var(--nav);display:flex;justify-content:center;align-items:center;
  font:14px Arial,sans-serif;color:#fff}
.footer span{margin:0 17px}
</style>
</head>
<body>
<div class="masthead"></div>

<div class="brand"><span class="brand-disc"></span><span class="brand-name">PVX</span></div>

<div class="abs lang"><span class="flag"><i style="background:#1f3fa0"></i><i style="background:#fff"></i><i style="background:#e0242b"></i></span>French<span class="caret"></span></div>

<nav class="abs nav">
  <a>Accueil</a><a>Procuvantix</a><a>Metiers</a><a>Non Referenced</a><a>Contact</a>
</nav>

<div class="abs field" style="left:694px">Username</div>
<div class="abs field" style="left:849px;color:#888;letter-spacing:2px">●●●●●●●</div>
<div class="abs login">Login</div>

<div class="abs slider">
  <div class="slide-photo" role="img" aria-label="Photo of four business people in a meeting around a table"></div>
  <div class="slide-caption">Achetez en toute simplicite</div>
</div>
<div class="abs dots"><i class="on"></i><i></i><i></i><i></i></div>

<section class="abs promo">
  <div class="promo-visual" role="img" aria-label="Illustration of a businessman pushing up a rising growth chart"></div>
  <svg class="abs" style="left:720px;top:0" width="200" height="166"><polygon points="160,0 200,0 80,166 0,166" fill="#9ea20a" opacity=".5"/><polygon points="175,0 200,0 110,166 80,166" fill="#eef0a8" opacity=".7"/></svg>
  <div class="promo-line1">Focus on your core</div>
  <div class="promo-line2">business &amp; call</div>
  <div class="promo-line3">a land experts.</div>
  <div class="promo-btn">More Details..</div>
</section>

<section class="abs card" style="left:103px">
  <h2>Actualites</h2>
  <ul class="news-list">
    <li>Beyond cost reduction</li><li>Purchasing have role</li><li>Beyond cost reduction</li>
    <li>Purchasing have&nbsp; role</li><li>Beyond cost reduction</li><li>Purchasing have&nbsp; role</li>
  </ul>
</section>

<section class="abs card" style="left:357px">
  <h2 style="margin-left:17px">Procuvantix</h2>
  <p>simply dummy text of the printing and typesetting industry. Lorem standard dummy text ever since the 1500s, when an unknown printer took a galley of type and make a type specimen book.</p>
  <span class="read-more">Read More »</span>
</section>

<section class="abs card" style="left:611px">
  <h2 style="margin-left:26px">Partenariats</h2>
  <svg class="abs" style="left:10px;top:92px" width="20" height="28"><path d="M14 3 4 14l10 11" fill="none" stroke="#333" stroke-width="3"/></svg>
  <div class="partner-frame"><span class="brand-disc"></span><span class="brand-name">PVX</span></div>
  <svg class="abs" style="left:205px;top:92px" width="20" height="28"><path d="M6 3l10 11L6 25" fill="none" stroke="#333" stroke-width="3"/></svg>
</section>

<section class="abs card newsletter" style="left:865px">
  <h2 style="margin-left:15px">Newsletter</h2>
  <p>Lorem Ipsum is simply dummy text of the printing typesetting industry.</p>
  <div class="mail">Insert Mail<b>Subscribe</b></div>
  <div class="social"><i></i><i></i><i></i><i></i></div>
</section>

<footer class="abs footer">
  <span>Mentions Legales</span>|<span>Plan du site</span>|<span>Procuvantix</span>|<span>Blog</span>
</footer>
</body>
</html>
```